Quiet Harbor Counseling Business Card design with a visually interesting use of Space

I need business cards that are luxurious and give a peaceful, calm vibe. I also had some letterhead designed, and i like the look of it also, it's attached with the logo design for reference/ ideas but feel free to be creative.

Target Market(s)

High end luxurious client who needs counseling

Industry/Entity Type

Marriage and Family Therapy

Contact Information for Business Card

Corra Mabbitt MS LMFT/ or Tobin Walsh address 4175 Pemberly Suite 620

Font styles to use
Sans Serif

Colors
0054AA
0677BA
7BADD7
CADEEF
E8F1F8
0094D4
00A9DD
6FCCEA
C7EBF8
E9F6FB
A7469A
B969AE
D3A5CF
EDDBEB
F8F0F9
6B429C
8869AF
B7A5CE
E3DAEB
F3F0F8

Requirements
Must have
• Logo and color scheme but be simple modern and luxurious
Nice to have
• I'd like to incorporate some elelmets from the logo and letterhead into a simple modern card

```html
<!DOCTYPE html>
<html lang="en">
<head>
<meta charset="utf-8">
<title>Quiet Harbor Counseling — Business Card</title>
<link href="https://fonts.googleapis.com/css2?family=Raleway:wght@200;300&family=Arimo:wght@400;700&display=swap" rel="stylesheet">
<style>
  :root {
    --page: #e4e4e4;
    --card-white: #ffffff;
    --card-dark: #2b2b2d;
    --pattern-light: #3a3a3d;
    --ink: #2a2a2a;
    --muted: #6d6d6d;
    --rule: #7a7a7a;
    --teal: #1f8c9a;
    --teal-band: #36b3be;
    --magenta: #a7469a;
    --purple: #8869af;
    --blue: #0677ba;
  }
  * { box-sizing: border-box; margin: 0; padding: 0; }
  html, body { width: 1200px; height: 802px; overflow: hidden; }
  body {
    background: var(--page);
    display: flex;
    align-items: center;
    justify-content: center;
    gap: 40px;
  }
  .card {
    width: 540px;
    height: 308px;
    position: relative;
    overflow: hidden;
    box-shadow: 0 6px 18px rgba(0,0,0,.18);
  }

  /* Front */
  .card-front { background: var(--card-white); }
  .brand {
    position: absolute;
    right: 40px;
    top: 42px;
    text-align: right;
    font-family: "Raleway", sans-serif;
    color: var(--ink);
  }
  .brand-mark {
    display: block;
    width: 34px; height: 34px;
    border-radius: 50%;
    background: var(--purple);
    margin: 0 0 10px auto;
  }
  .brand-name {
    font-weight: 300;
    font-size: 40px;
    line-height: 1;
    letter-spacing: .5px;
  }
  .brand-tag {
    font-weight: 300;
    font-size: 15px;
    letter-spacing: 4px;
    margin-top: 4px;
  }
  .divider {
    position: absolute;
    left: 40px; right: 40px;
    top: 168px;
    height: 1px;
    background: var(--rule);
  }
  .address {
    position: absolute;
    right: 40px;
    top: 180px;
    text-align: right;
    font-family: "Arimo", sans-serif;
    font-size: 12px;
    line-height: 1.35;
    color: var(--muted);
  }
  .person {
    position: absolute;
    left: 40px;
    top: 186px;
    font-family: "Arimo", sans-serif;
  }
  .person-name {
    color: var(--teal);
    font-weight: 700;
    font-size: 18px;
    letter-spacing: .3px;
    text-transform: uppercase;
  }
  .person-title {
    color: var(--muted);
    font-size: 12px;
    margin-top: 1px;
    padding-bottom: 5px;
    border-bottom: 1px solid var(--rule);
    width: 150px;
  }
  .contacts {
    list-style: none;
    margin-top: 5px;
    font-size: 11.5px;
    color: var(--muted);
    line-height: 1.35;
  }
  .contacts li { display: flex; align-items: center; gap: 6px; }
  .contacts svg { width: 10px; height: 10px; fill: var(--teal); flex: none; }
  .edge-band {
    position: absolute;
    left: 0; right: 0; bottom: 0;
    height: 8px;
    display: flex;
  }
  .edge-band span { height: 100%; }
  .band-purple { background: var(--purple); flex: 1; }
  .band-magenta { background: var(--magenta); flex: 2.4; border-left: 2px solid #fff; }
  .band-teal { background: var(--teal-band); flex: 1.2; border-left: 2px solid #fff; }

  /* Back */
  .card-back { background: var(--card-dark); }
  .back-pattern {
    position: absolute; inset: 0;
    background: radial-gradient(ellipse at 80% 30%, #4a4a4e 0%, var(--pattern-light) 35%, var(--card-dark) 80%);
  }
  .back-brand {
    position: absolute;
    right: 44px;
    top: 104px;
    text-align: right;
    font-family: "Raleway", sans-serif;
    color: #ffffff;
  }
  .back-brand .brand-mark { background: var(--magenta); width: 40px; height: 40px; }
  .back-brand .brand-name { font-size: 42px; font-weight: 200; }
  .back-brand .brand-tag { font-size: 16px; font-weight: 200; }
</style>
</head>
<body>
  <section class="card card-front" aria-label="Business card front">
    <div class="brand">
      <span class="brand-mark"></span>
      <div class="brand-name">Quiet Harbor</div>
      <div class="brand-tag">Counseling</div>
    </div>
    <div class="divider"></div>
    <address class="address">
      4175 pemberly suite 620<br>
      harbor falls<br>
      alaska 34510
    </address>
    <div class="person">
      <div class="person-name">Corra Mabbitt</div>
      <div class="person-title">MS LMFT</div>
      <ul class="contacts">
        <li><svg viewBox="0 0 10 10"><path d="M2 0.5l2 2-1 1.2c.6 1.3 1.6 2.3 2.9 2.9l1.2-1 2 2-1.3 1.6C4.2 9 1 5.8.5 1.8z"/></svg>369-480-2716</li>
        <li><svg viewBox="0 0 10 10"><rect x="2" y="0.5" width="6" height="3"/><rect x="0.5" y="3.5" width="9" height="4" rx="1"/><rect x="2" y="6.5" width="6" height="3"/></svg>369-480-2790</li>
        <li><svg viewBox="0 0 10 10"><path d="M0.5 2h9v6h-9z M0.5 2l4.5 3.5L9.5 2" stroke="#fff" stroke-width=".8"/></svg>info@quietharbor.com</li>
        <li><svg viewBox="0 0 10 10"><circle cx="5" cy="5" r="4.5"/><path d="M0.5 5h9M5 .5c2 2.5 2 6.5 0 9M5 .5c-2 2.5-2 6.5 0 9" stroke="#fff" stroke-width=".7" fill="none"/></svg>www.quietharbor.com</li>
      </ul>
    </div>
    <div class="edge-band">
      <span class="band-purple"></span>
      <span class="band-magenta"></span>
      <span class="band-teal"></span>
    </div>
  </section>

  <section class="card card-back" aria-label="Business card back">
    <div class="back-pattern" role="img" aria-label="Embossed repeating pattern of outlined thought-bubble clusters in glossy grey on charcoal"></div>
    <div class="back-brand">
      <span class="brand-mark"></span>
      <div class="brand-name">Quiet Harbor</div>
      <div class="brand-tag">Counseling</div>
    </div>
  </section>
</body>
</html>
```